New Packaging and label for New Beard Oil and Shampoo brand from London

Oils, Shampoo ect .. Beard Oil Ingredients: Application Directions: Apply to beard by weight in a small amount of oil will naturally absorb. Leaving it soft & conditioned. Ingredients: Coconut oil, scented oil, Oud oil, vitamin E 100% Natural `i will have 5 types of oils Vanilla Oud Rose Oud Cocktail Tea tree Arabian Night

Target Market(s)

A fashionable well groomed professional gentleman who is willing to invest in his appearance.

Industry/Entity Type

It Company

Font styles to use
Sans Serif

Colors

Designer to choose colors to be used in the design.

Requirements
Must have
• Beard Oil Ingredients: Application Directions: Apply to a beard by a small amount of oil will naturally absorb. Leaving it soft & conditioned. Ingredients: Coconut Oil, Scented Oil, Oil Oud, Vitamin E 100% Natural 1.0z 30ml Made in Uk i will have 5 types of oils Vanilla Oud Rose Oud Cocktail Tea Tree Arabian Beard Night Shampoo APPLICATION DIRECTIONS Massage into the beard / hair and rinse out with warm water. Distorted shampoos, there are no nasty chemicals which are damaging your beard instead of the wheat proteins and oils that you add to the hair follicles with nutrients and naturally adding a protective coating. INGREDIENTS Aqua (Water), Capryl / caprylyl glucoside, Cocomidopropyl betaine, Glycerin (Veg), Xanthan gum, Phenoxyethanol, Hydrolysed wheat protein, Aloe barbadensis (Aloe vera) leaf powder, Sodium benzoate, Potassium sorbate1 3.4 oz, 100ml Cylinder packaging for the Oils, Box for the shampoo
Nice to have
• I want "London" written underneath the logo and oil name.

```html
<!DOCTYPE html>
<html lang="en">
<head>
<meta charset="utf-8">
<title>Fairhaven Grooming – Beard Shampoo Box</title>
<link href="https://fonts.googleapis.com/css2?family=Lato:wght@400;700;900&family=Roboto+Condensed:wght@400;700&family=Kaushan+Script&display=swap" rel="stylesheet">
<style>
  :root {
    --backdrop: #e6e6e6;
    --board: #ffffff;
    --ink: #2a2a2a;
    --gold: #c9a23f;
    --gold-soft: #dcc27a;
    --placeholder-light: #d4d4d4;
    --placeholder-dark: #a9a9a9;
  }
  * { box-sizing: border-box; margin: 0; padding: 0; }
  html, body { width: 1200px; height: 1200px; overflow: hidden; }
  body {
    background: var(--backdrop);
    font-family: "Lato", sans-serif;
    color: var(--ink);
    position: relative;
  }
  .dieline {
    position: absolute;
    left: 240px; top: 240px;
    width: 720px; height: 720px;
    display: flex;
    box-shadow: 0 10px 30px rgba(0,0,0,0.08);
  }
  .panel {
    position: relative;
    background: var(--board);
    height: 720px;
  }
  .panel--side { width: 300px; border-right: 1px solid #ececec; }
  .panel--front { width: 420px; }

  .rule-band {
    position: absolute;
    height: 8px;
    border-top: 2px dotted var(--gold);
    border-bottom: 2px dotted var(--gold);
  }
  .panel--side .rule-band { top: 76px; left: 0; width: 300px; }
  .front-band-left { top: 76px; left: 0; width: 130px; }
  .front-band-right { top: 76px; right: 0; width: 130px; }

  .directions-frame {
    position: absolute;
    left: 22px; top: 150px;
    width: 256px; height: 300px;
    border: 1.5px solid var(--gold);
    outline: 1px solid var(--gold-soft);
    outline-offset: -6px;
    padding: 16px;
  }
  .side-heading {
    font-family: "Roboto Condensed", sans-serif;
    font-size: 14px;
    color: var(--gold);
    text-transform: uppercase;
    letter-spacing: 0.3px;
    margin-bottom: 4px;
  }
  .side-copy {
    font-family: "Roboto Condensed", sans-serif;
    font-size: 15px;
    line-height: 1.38;
    color: var(--ink);
  }
  .ingredients {
    position: absolute;
    left: 30px; top: 470px; width: 244px;
  }
  .side-volume {
    position: absolute; left: 30px; top: 640px;
    font-family: "Roboto Condensed", sans-serif; font-size: 14px;
  }
  .side-origin {
    position: absolute; left: 30px; top: 680px;
    font-family: "Roboto Condensed", sans-serif; font-size: 14px; font-weight: 700;
    color: var(--gold);
  }

  .brand-mark {
    position: absolute;
    top: 66px; left: 130px; width: 160px;
    display: flex; align-items: center; justify-content: center; gap: 6px;
    font-weight: 900;
    font-size: 19px; letter-spacing: 0.5px;
    color: var(--ink);
  }
  .brand-mark .mark-square { width: 10px; height: 10px; background: var(--gold); }
  .city {
    position: absolute; top: 160px; left: 0; width: 420px;
    text-align: center;
    font-size: 14px; letter-spacing: 1.5px;
    color: var(--gold);
  }
  .emblem-frame { position: absolute; left: 0; top: 0; }
  .landmark-art {
    position: absolute; left: 150px; top: 186px;
    width: 120px; height: 42px;
    background: linear-gradient(180deg, var(--placeholder-light), var(--placeholder-dark));
  }
  .badge-note {
    position: absolute;
    font-family: "Roboto Condensed", sans-serif;
    font-size: 12px; color: var(--ink);
    white-space: nowrap;
  }
  .badge-note--left { left: 62px; top: 250px; transform: rotate(-52deg); }
  .badge-note--right { left: 272px; top: 250px; transform: rotate(52deg); }
  .product-title {
    position: absolute; top: 270px; left: 0; width: 420px;
    text-align: center; line-height: 1;
    font-weight: 900;
  }
  .product-title .line-1 { display: block; font-size: 46px; letter-spacing: 0.5px; }
  .product-title .line-2 { display: block; font-size: 30px; margin-top: 4px; font-weight: 700; }
  .beard-art {
    position: absolute; left: 122px; top: 378px;
    width: 176px; height: 150px;
    background: linear-gradient(180deg, var(--placeholder-light), var(--placeholder-dark));
  }
  .scent-name {
    position: absolute; top: 572px; left: 0; width: 420px;
    text-align: center;
    font-family: "Kaushan Script", cursive;
    font-size: 42px; color: var(--ink);
    transform: rotate(-5deg);
  }
  .scent-rules { position: absolute; left: 0; top: 540px; }
</style>
</head>
<body>
  <main class="dieline">
    <section class="panel panel--side" aria-label="Side panel">
      <div class="rule-band"></div>
      <div class="directions-frame">
        <h3 class="side-heading">Application Directions</h3>
        <p class="side-copy">Massage into the beard/hair and rinse out with warm water. Unlike conventional shampoo, there are no nasty chemicals which are damaging your beard instead the wheat proteins and oils which you have added are filling the hair follicles with nutrients and naturally adding a protective coating.</p>
      </div>
      <div class="ingredients">
        <h3 class="side-heading">Ingredients</h3>
        <p class="side-copy">Aqua (Water), Capryl/caprylyl glucoside, Cocamidopropyl betaine, Glycerine (Veg), Xanthan gum, Phenoxyethanol, Hydrolysed wheat protein, Aloe barbadensis (Aloe vera) leaf powder, Sodium benzoate, Potassium sorbate</p>
      </div>
      <p class="side-volume">3.4 OZ. 100 ML</p>
      <p class="side-origin">MADE IN UK</p>
    </section>

    <section class="panel panel--front" aria-label="Front panel">
      <div class="rule-band front-band-left"></div>
      <div class="rule-band front-band-right"></div>
      <div class="brand-mark"><span class="mark-square"></span>FAIRHAVEN</div>

      <p class="city">LONDON</p>

      <svg class="emblem-frame" width="420" height="720" viewBox="0 0 420 720" aria-hidden="true">
        <polyline points="150,232 90,300 150,368" fill="none" stroke="var(--gold)" stroke-width="1.5"/>
        <polyline points="270,232 330,300 270,368" fill="none" stroke="var(--gold)" stroke-width="1.5"/>
        <line x1="150" y1="232" x2="270" y2="232" stroke="var(--gold)" stroke-width="1.5"/>
      </svg>
      <div class="landmark-art" role="img" aria-label="Engraved illustration of a London bridge"></div>
      <span class="badge-note badge-note--left">100% NATURAL</span>
      <span class="badge-note badge-note--right">3.4 OZ • 100 ML</span>

      <h1 class="product-title"><span class="line-1">BEARD</span><span class="line-2">SHAMPOO</span></h1>

      <div class="beard-art" role="img" aria-label="Engraved illustration of a full beard and moustache"></div>

      <svg class="scent-rules" width="420" height="120" viewBox="0 0 420 120" aria-hidden="true">
        <path d="M70 30 Q210 0 350 30" fill="none" stroke="var(--gold)" stroke-width="1.5"/>
        <path d="M90 95 Q210 120 330 95" fill="none" stroke="var(--gold)" stroke-width="1.5"/>
      </svg>
      <p class="scent-name">Vanilla Oud</p>
    </section>
  </main>
</body>
</html>
```